Luxury Wine Label for New Startup Winery

We need a wine label for our new winery startup. We have worked with a local designer but do not feel the resulting label / logo have the elevation required to present our brand as a luxury wine. Our winery is called "Harrowgate Vineyards" and we are focused on extremely high quality hand crafted artisan and estate wines from the Pacific Northwest.
We would like to see designs that utilize a tree line, or other imagery that represents the "Harrowgate" part of our company name. Another interesting feature could be wood grain.
A logo will be required based on your design so please design with this in mind:
This logo should be consistent with the wine bottle label design, and should be representative of our high end exclusive wine while giving a sense of place (Oregon/ Pacific Northwest.)
I will supply an image of the design we received from our local designer, PLEASE NOTE: in general we do like wood grain and tree line concepts but feel the execution was poorly done.
ATTN: Logo design should be suitable for use on: Bottles (Red wine/rose/white wine), Bussiness cards, vehicle signage, business signage, etc
P.S.:
If you have a design that is not outside the box we are still interested in seeing it.
Label is for a burgundy style bottle with a label height of 3.5 - 4" and a width of 3.5-4"
any label <= 4"x4" and >=3.5"x3.5" will be acceptable:
HOWEVER Width should be greater than or equal to height due to the bottle format
Target Market(s)
Wine enthusiasts with adequate discretionary budgets to afford $100 bottles of wine.
Industry/Entity Type
Wine / Winery
Requirements
Must have
- A sense of luxury, a feel of exclusivity, and a theme consistent with our product and brand name
Nice to have
- Tree line, wood grain or other wood themes. Serif fonts
Should not have
- anything cheesy, off topic, hard to read script fonts or anything that makes the label hard to read from a few feet away or too busy

```html
<!DOCTYPE html>
<html lang="en">
<head>
<meta charset="utf-8">
<title>Harrowgate Vineyards – Syrah Label</title>
<link rel="stylesheet" href="https://fonts.googleapis.com/css2?family=Cormorant+Garamond:wght@400;500&display=swap">
<style>
  :root {
    --canvas: #f4f4f4;
    --label-black: #0f0f0f;
    --label-black-soft: #1c1c1c;
    --gold: #c9a24c;
    --silver: #cfcfcf;
    --ink: #141414;
    --ink-soft: #3a3328;
    --wood-light: #e9c98a;
    --wood-mid: #d4a85c;
    --wood-deep: #c0914a;
  }
  * { margin: 0; padding: 0; box-sizing: border-box; }
  html, body {
    width: 1200px;
    height: 1098px;
    overflow: hidden;
    background: var(--canvas);
  }
  .label-set {
    position: absolute;
    left: 144px;
    top: 66px;
    width: 912px;
  }
  .main-label {
    position: relative;
    width: 912px;
    height: 738px;
    border-radius: 30px;
    background: linear-gradient(160deg, var(--label-black-soft) 0%, var(--label-black) 60%, #090909 100%);
    text-align: center;
    font-family: "Cormorant Garamond", "Times New Roman", serif;
  }
  .brand-mark {
    position: absolute;
    left: 50%;
    top: 150px;
    width: 120px;
    height: 120px;
    margin-left: -60px;
    border: 2px solid var(--gold);
    border-radius: 50%;
  }
  .brand-name {
    position: absolute;
    left: 0;
    right: 0;
    top: 320px;
    color: var(--gold);
    font-weight: 500;
    line-height: 1.05;
  }
  .brand-name .primary {
    display: block;
    font-size: 104px;
    letter-spacing: 2px;
  }
  .brand-name .secondary {
    display: block;
    font-size: 50px;
    letter-spacing: 12px;
    margin-top: 14px;
  }
  .region {
    position: absolute;
    left: 0;
    right: 0;
    top: 634px;
    color: var(--silver);
    font-size: 31px;
    font-weight: 400;
    letter-spacing: 15px;
    opacity: 0.85;
  }
  .variety-band {
    position: relative;
    width: 912px;
    height: 195px;
    margin-top: 33px;
    border-radius: 30px;
    background: linear-gradient(90deg, var(--wood-mid) 0%, var(--wood-light) 22%, var(--wood-deep) 40%, var(--wood-light) 58%, var(--wood-mid) 78%, var(--wood-light) 100%);
    text-align: center;
    font-family: "Cormorant Garamond", "Times New Roman", serif;
  }
  .variety {
    position: absolute;
    left: 0;
    right: 0;
    top: 30px;
    color: var(--ink);
    font-size: 80px;
    font-weight: 400;
    letter-spacing: 8px;
    line-height: 1;
  }
  .vintage {
    position: absolute;
    left: 0;
    right: 0;
    top: 128px;
    color: var(--ink-soft);
    font-size: 27px;
    font-weight: 500;
    letter-spacing: 4px;
  }
</style>
</head>
<body>
  <div class="label-set">
    <section class="main-label" role="img" aria-label="Black wood-grain label background">
      <span class="brand-mark" aria-hidden="true"></span>
      <h1 class="brand-name">
        <span class="primary">Harrowgate</span>
        <span class="secondary">VINEYARDS</span>
      </h1>
      <p class="region">WILLAMETTE VALLEY</p>
    </section>
    <section class="variety-band" role="img" aria-label="Light golden wood-grain band">
      <h2 class="variety">SYRAH</h2>
      <p class="vintage">ESTATE | 2023 | GROWN</p>
    </section>
  </div>
</body>
</html>
```